Business card design for Sable Crestway

We need business cards designed for our new marketing consulting company, Sable Crestway. Our services include marketing strategy, go-to-market and launch planning, growth strategy, and execution. We serve medical technology and health technology companies, from startups to well-established growth companies.

The business cards should feel professional, credible, reliable and trustworthy, and should instill confidence. Also bold, creative, and modern.

The design must use the Sable Crestway logo.

The primary brand color is this orange: #FF5501
A secondary color that you can use is this gray: #282B2D
I would prefer only to use the orange and gray. But if you feel you really need an additional accent color (please use it very sparingly, as little as possible), you can use this blue for small accent purposes: #009FED

Attached are the logo files. The main logo is the one with a little bit of orange on the left and the rest is gray.

The business card should include the following:

Sable Crestway logo
First name and last name
Title
Email address
Phone number and type (in whatever order looks best for the design
Website (the website does not need to be in the same block as the personal info)

For example:

Wren Tasker
Founder & Principal
wren@sablecrestway.com
+1.415.836.2094 mobile (can use "." or spaces in between blocks of numbers)
sablecrestway.com (somewhere on the card, it does not need to be with the personal info; and note that there is no "www." at the beginning)

Note that there will be no address listed on the business card.

Target Market(s)

Executives (CEO, head of marketing, head of sales) at medical technology and health technology companies, mostly in their 40s and older, well-educated, often with advanced degrees. They are strategic thinkers, responsible for budgets, and familiar with P&L. Their comfort with and trust in using outside consultants varies.

Industry/Entity Type

Medical technology and health technology companies.

Contact Information for Business Card

See project description

Font styles to use
Sans Serif

Requirements
Must have
• Logo and see Business card details section above.

```html
<!DOCTYPE html>
<html lang="en">
<head>
<meta charset="utf-8">
<title>Sable Crestway — Business Card</title>
<link rel="stylesheet" href="https://fonts.googleapis.com/css2?family=Inter:wght@400;600;700&display=swap">
<style>
  :root {
    --brand-orange: #FF5501;
    --brand-gray: #282B2D;
    --accent-blue: #009FED;
    --stage: #E9EAE9;
    --paper: #FBFBFB;
    --edge: #9A9C9D;
  }
  * { margin: 0; padding: 0; box-sizing: border-box; }
  html, body { width: 1200px; height: 905px; overflow: hidden; }
  body {
    background: var(--stage);
    font-family: "Inter", "Helvetica Neue", Arial, sans-serif;
    position: relative;
  }
  .card {
    position: absolute;
    left: 264px;
    width: 686px;
    overflow: hidden;
  }
  .card--front { top: 31px; height: 414px; background: var(--brand-orange); }
  .card--back { top: 455px; height: 415px; background: var(--paper); border: 1px solid var(--edge); }

  .front-pattern {
    position: absolute; inset: 0;
    background: radial-gradient(ellipse at 40% 45%, rgba(255,120,60,0.35), rgba(255,85,1,0) 70%);
  }

  .wordmark {
    position: absolute;
    display: flex;
    align-items: center;
    gap: 16px;
  }
  .wordmark__dot { width: 46px; height: 46px; border-radius: 50%; flex: none; }
  .wordmark__name {
    font-weight: 600;
    font-size: 23px;
    line-height: 25px;
    letter-spacing: 0.2em;
    text-transform: uppercase;
  }
  .card--front .wordmark { left: 368px; top: 233px; }
  .card--front .wordmark__dot { background: #FFFFFF; }
  .card--front .wordmark__name { color: #FFFFFF; }
  .card--back .wordmark { left: 368px; top: 61px; }
  .card--back .wordmark__dot { background: var(--brand-orange); }
  .card--back .wordmark__name { color: var(--brand-gray); }

  .identity {
    position: absolute;
    left: 29px; top: 216px;
    padding-left: 16px;
    border-left: 2px solid var(--brand-orange);
    height: 51px;
  }
  .identity__name {
    font-weight: 700;
    font-size: 30px;
    line-height: 30px;
    letter-spacing: -0.03em;
    color: var(--brand-gray);
    margin-top: -1px;
  }
  .identity__title {
    font-weight: 400;
    font-size: 15.5px;
    line-height: 20px;
    color: var(--brand-orange);
  }

  .contacts {
    position: absolute;
    left: 47px; top: 299px;
    list-style: none;
  }
  .contacts__item {
    display: flex;
    align-items: center;
    height: 24.5px;
    font-size: 17px;
    color: var(--brand-gray);
  }
  .contacts__icon { width: 16px; height: 16px; margin-right: 13px; flex: none; }

  .band { position: absolute; bottom: 0; height: 15px; }
  .band--orange { left: 0; width: 236px; background: var(--brand-orange); }
  .band--gray { left: 248px; right: 0; background: var(--brand-gray); }

  .guide { position: absolute; background: var(--accent-blue); opacity: 0.7; }
  .guide--top { left: 249px; top: 675px; width: 203px; height: 1px; }
  .guide--base { left: 249px; top: 722px; width: 203px; height: 1px; }
  .guide--column { left: 500px; top: 805px; width: 1px; height: 100px; }
</style>
</head>
<body>
  <section class="card card--front">
    <div class="front-pattern" role="img" aria-label="Faint repeating brand pattern in lighter orange"></div>
    <div class="wordmark">
      <span class="wordmark__dot"></span>
      <span class="wordmark__name">Sable<br>Crestway</span>
    </div>
  </section>

  <section class="card card--back">
    <div class="wordmark">
      <span class="wordmark__dot"></span>
      <span class="wordmark__name">Sable<br>Crestway</span>
    </div>

    <div class="identity">
      <h1 class="identity__name">Wren Tasker</h1>
      <p class="identity__title">Founder &amp; Principal</p>
    </div>

    <ul class="contacts">
      <li class="contacts__item">
        <svg class="contacts__icon" viewBox="0 0 16 16" fill="none" stroke="#FF5501" stroke-width="1.3">
          <circle cx="8" cy="8" r="7"/>
          <path d="M5.3 4.6l1.4 1.6-.7 1c.6 1.2 1.4 2 2.6 2.6l1-.7 1.6 1.4-.8 1.1c-2.8-.4-5.2-2.8-5.6-5.6z" stroke-linejoin="round"/>
        </svg>
        +1.415.836.2094
      </li>
      <li class="contacts__item">
        <svg class="contacts__icon" viewBox="0 0 16 16" fill="none" stroke="#FF5501" stroke-width="1.3">
          <rect x="1" y="3" width="14" height="10" rx="1"/>
          <path d="M1.5 3.6L8 9l6.5-5.4M1.5 12.4L6 8m8.5 4.4L10 8"/>
        </svg>
        wren@sablecrestway.com
      </li>
      <li class="contacts__item">
        <svg class="contacts__icon" viewBox="0 0 16 16" fill="none" stroke="#FF5501" stroke-width="1.2">
          <circle cx="8" cy="8" r="7"/>
          <ellipse cx="8" cy="8" rx="3" ry="7"/>
          <path d="M1 8h14M2 4.5h12M2 11.5h12"/>
        </svg>
        sablecrestway.com
      </li>
    </ul>

    <div class="band band--orange"></div>
    <div class="band band--gray"></div>
  </section>

  <div class="guide guide--top"></div>
  <div class="guide guide--base"></div>
  <div class="guide guide--column"></div>
</body>
</html>
```